PowerPoint Design TELM

I have now selected the logo for my consultancy company. I need some innovative design for my Powerpoint slides. The audience is senior executives in international banks predominantly in Asia, but also in the Middle East, Africa and Latin America.
My company advises them on solutions to be able to grow their business.
This is my main means of hooking the clients and it is crucial to the success of my business.
I will update the file to a vector file in a few hours.

I am looking for a complete template.

Senior hard nosed executives in international Banks

```html
<!DOCTYPE html>
<html lang="en">
<head>
<meta charset="utf-8">
<title>TELM Slide Template</title>
<link rel="stylesheet" href="https://fonts.googleapis.com/css2?family=Exo+2:wght@400;500&family=Arimo&display=swap">
<style>
  :root {
    --green: #1fb35c;
    --ink-dark: #3c3c3c;
    --ink-body: #6a6a6a;
    --ink-strong: #3a3a3a;
    --rule: #d2d4d8;
    --band-top: #ffffff;
    --band-bottom: #eeeeef;
    --stage-top: #f6f6f6;
    --stage-bottom: #e3e5ea;
    --card: #ffffff;
    --card-edge: #dddddd;
  }
  * { margin: 0; padding: 0; box-sizing: border-box; }
  html, body { width: 1200px; height: 900px; overflow: hidden; }
  body { font-family: "Exo 2", sans-serif; background: var(--stage-top); }

  .slide {
    position: relative;
    width: 1200px;
    height: 900px;
    background: linear-gradient(180deg, var(--stage-top) 0%, var(--stage-top) 60%, var(--stage-bottom) 100%);
    overflow: hidden;
  }
  .slide-texture {
    position: absolute;
    left: 0; top: 98px;
    width: 1200px; height: 714px;
    background:
      radial-gradient(ellipse 520px 420px at 180px 380px, rgba(200,202,206,0.35), rgba(200,202,206,0) 70%),
      radial-gradient(ellipse 700px 260px at 600px 700px, rgba(205,208,214,0.35), rgba(205,208,214,0) 70%);
  }

  .header-band {
    position: absolute;
    left: 0; top: 0;
    width: 1200px; height: 98px;
    background: linear-gradient(180deg, var(--band-top) 0%, var(--band-bottom) 100%);
    border-bottom: 2px solid var(--rule);
  }
  .slide-title {
    position: absolute;
    left: 30px; top: 22px;
    font-size: 45px;
    font-weight: 400;
    color: var(--green);
    letter-spacing: 0.5px;
  }

  .content-title {
    position: absolute;
    left: 66px; top: 154px;
    font-size: 35px;
    font-weight: 400;
    color: var(--ink-dark);
  }
  .content-title .accent { color: var(--green); }

  .body-copy {
    position: absolute;
    left: 66px; top: 225px;
    width: 531px;
  }
  .body-copy p {
    font-size: 20.5px;
    line-height: 39px;
    color: var(--ink-body);
    text-align: justify;
    margin-bottom: 39px;
  }
  .body-copy strong { font-weight: 500; color: var(--ink-strong); }

  .photo-slot {
    position: absolute;
    left: 708px;
    width: 445px; height: 197px;
    background: var(--card);
    border: 1.5px solid var(--card-edge);
    border-radius: 6px;
    box-shadow: 0 2px 5px rgba(0,0,0,0.08);
    display: flex; align-items: center; justify-content: center;
    font-size: 21px; font-weight: 500; color: #555;
  }
  .photo-slot.first { top: 226px; }
  .photo-slot.second { top: 496px; }

  .footer-band {
    position: absolute;
    left: 0; top: 812px;
    width: 1200px; height: 88px;
    background: linear-gradient(180deg, #f7f7f7 0%, #ffffff 100%);
    border-top: 2px solid var(--rule);
  }
  .copyright {
    position: absolute;
    left: 28px; top: 35px;
    font-family: "Arimo", sans-serif;
    font-size: 19px;
    color: #111;
  }
  .brand-name {
    position: absolute;
    right: 30px; top: 24px;
    font-family: "Exo 2", sans-serif;
    font-size: 32px;
    font-weight: 500;
    color: var(--green);
  }
</style>
</head>
<body>
  <main class="slide">
    <div class="slide-texture" role="img" aria-label="Soft grey dotted background texture"></div>

    <header class="header-band">
      <h1 class="slide-title">Insert Title Here</h1>
    </header>

    <h2 class="content-title">Content <span class="accent">Title Here</span></h2>

    <section class="body-copy">
      <p><strong>Lorem ipsum dolor sit ipsum</strong> Lorem ipsum dolor sit ipsum Lorem ipsum Lorem ipsum dolor sit ipsum Lorem ipsum dolor sit ipsum Lorem ipsum.</p>
      <p><strong>Lorem ipsum dolor sit</strong> ipsum Lorem ipsum dolor sit ipsum Lorem ipsum Lorem ipsum dolor sit ipsum Lorem ipsum dolor sit ipsum Lorem ipsum.</p>
      <p>Lorem ipsum dolor sit ipsum Lorem ipsum dolor sit ipsum Lorem ipsum Lorem ipsum dolor sit ipsum Lorem ipsum dolor sit ipsum Lorem ipsum.</p>
    </section>

    <div class="photo-slot first">Photo Here</div>
    <div class="photo-slot second">Photo Here</div>

    <footer class="footer-band">
      <span class="copyright">Copyright Text here</span>
      <span class="brand-name">TELM</span>
    </footer>
  </main>
</body>
</html>
```